Medical IT Business with New logo needs a fresh stationary design

First time on sketch Harbor; Thought I would give it a go.
This project is for business cards alone but we have loads of design work that needs to take place in the immediate future.

We provide IT services to the Medical Industry and value ourselves as offering a premium product to the market.

I am after a fresh, clean design using full colour 2 sided cards which includes our current colour palettes from our logo.

Card's must include:
- Logo
- Slogan
- Name
- Adress
- Email
- Phone
- Fax
- Mobile

Target Market(s)

Surgeons, High Profile Medical Personnel

Industry/Entity Type

Business

Fonts, CMYK Colours and Logo files attached.

Requirements
Must have
• Card's must include:
• - Logo
• - Slogan
• - Name
• - Adress
• - Email
• - Phone
• - Fax
• - Mobile
Nice to have
• Needs to incorporate our colour palette (attached CMYK colours)
Should not have
• Black backgrounds. Black text ok.

```html
<!DOCTYPE html>
<html lang="en">
<head>
<meta charset="utf-8">
<title>Pulsewise Systems – Business Cards</title>
<link rel="stylesheet" href="https://fonts.googleapis.com/css2?family=Open+Sans:wght@400;600;700&display=swap">
<style>
  :root {
    --page-bg: #e4e9ec;
    --brand-blue: #0a7bb5;
    --brand-navy: #1a3567;
    --slogan-grey: #8a93a8;
    --card-white: #ffffff;
    --card-mist: #f2f3f5;
    --card-shadow: rgba(26, 53, 103, 0.14);
  }
  * { box-sizing: border-box; margin: 0; padding: 0; }
  html, body {
    width: 1200px; height: 900px; overflow: hidden;
    background: var(--page-bg);
    font-family: "Open Sans", Arial, sans-serif;
  }
  .sheet {
    width: 1200px; height: 900px;
    display: flex; flex-direction: column; align-items: center; justify-content: center;
    gap: 20px;
  }
  .card {
    position: relative;
    width: 700px; height: 400px;
    box-shadow: 0 6px 22px var(--card-shadow);
    overflow: hidden;
  }

  /* Brand lockup: plain square + name + slogan */
  .brand { display: flex; align-items: center; gap: 14px; }
  .brand-square { background: var(--brand-blue); flex: none; }
  .brand-name {
    font-weight: 700; color: var(--brand-navy);
    letter-spacing: 0.5px; text-transform: uppercase; line-height: 1;
  }
  .brand-slogan { color: var(--slogan-grey); margin-top: 6px; line-height: 1.2; }

  /* Back side */
  .card-back { background: var(--card-white); display: flex; align-items: center; justify-content: center; }
  .card-back .brand-square { width: 40px; height: 40px; }
  .card-back .brand-name { font-size: 38px; }
  .card-back .brand-slogan { font-size: 17px; }

  /* Front side */
  .card-front { background: var(--card-mist); display: flex; }
  .identity-panel {
    width: 280px; height: 100%;
    background: var(--brand-blue);
    color: var(--card-white);
    text-align: right;
    padding: 64px 36px 0 0;
  }
  .person-name { font-size: 30px; font-weight: 700; line-height: 1.1; }
  .person-role { font-size: 19px; margin-top: 4px; }
  .person-mobile { font-size: 17px; margin-top: 4px; }

  .info-side { position: relative; flex: 1; padding: 40px 0 0 40px; }
  .info-side .brand-square { width: 28px; height: 28px; }
  .info-side .brand-name { font-size: 25px; }
  .info-side .brand-slogan { font-size: 13px; margin-top: 4px; }

  .contact-rail {
    position: absolute; left: -30px; top: 142px;
    width: 60px; height: 216px;
    background: var(--card-white); border-radius: 12px;
  }
  .contact-list { list-style: none; position: absolute; left: -22px; top: 152px; }
  .contact-item {
    display: flex; align-items: center; gap: 16px;
    height: 50px; color: var(--brand-navy); font-size: 16px; line-height: 1.25;
  }
  .contact-icon {
    width: 44px; height: 44px; border-radius: 50%;
    background: var(--brand-navy);
    display: flex; align-items: center; justify-content: center; flex: none;
  }
  .contact-icon svg { width: 22px; height: 22px; fill: var(--card-white); }
</style>
</head>
<body>
<main class="sheet">

  <section class="card card-back" aria-label="Business card, back">
    <div class="brand">
      <span class="brand-square"></span>
      <div>
        <div class="brand-name">Pulsewise Systems</div>
        <div class="brand-slogan">care systems, always on</div>
      </div>
    </div>
  </section>

  <section class="card card-front" aria-label="Business card, front">
    <div class="identity-panel">
      <div class="person-name">Jordan Vale</div>
      <div class="person-role">Director</div>
      <div class="person-mobile">0198 765 432</div>
    </div>

    <div class="info-side">
      <div class="brand">
        <span class="brand-square"></span>
        <div>
          <div class="brand-name">Pulsewise Systems</div>
          <div class="brand-slogan">care systems, always on</div>
        </div>
      </div>

      <div class="contact-rail"></div>
      <ul class="contact-list">
        <li class="contact-item">
          <span class="contact-icon"><svg viewBox="0 0 24 24" aria-hidden="true"><path d="M6.6 10.8a15.1 15.1 0 0 0 6.6 6.6l2.2-2.2a1 1 0 0 1 1-.25 11.4 11.4 0 0 0 3.6.57 1 1 0 0 1 1 1V20a1 1 0 0 1-1 1A17 17 0 0 1 3 4a1 1 0 0 1 1-1h3.5a1 1 0 0 1 1 1c0 1.25.2 2.450.57 3.57a1 1 0 0 1-.25 1z"/></svg></span>
          <span>0198 765 432</span>
        </li>
        <li class="contact-item">
          <span class="contact-icon"><svg viewBox="0 0 24 24" aria-hidden="true"><path d="M7 3h10v4H7zM4 8h16a2 2 0 0 1 2 2v6h-4v5H6v-5H2v-6a2 2 0 0 1 2-2zm4 7v4h8v-4z"/></svg></span>
          <span>0198 765 433</span>
        </li>
        <li class="contact-item">
          <span class="contact-icon"><svg viewBox="0 0 24 24" aria-hidden="true"><path d="M3 5h18a1 1 0 0 1 1 1v12a1 1 0 0 1-1 1H3a1 1 0 0 1-1-1V6a1 1 0 0 1 1-1zm1 2.3V17h16V7.3l-8 5.2z M4.6 7l7.4 4.8L19.4 7z"/></svg></span>
          <span>jordanvale@mailbox.com</span>
        </li>
        <li class="contact-item">
          <span class="contact-icon"><svg viewBox="0 0 24 24" aria-hidden="true"><path d="M12 2a7 7 0 0 1 7 7c0 5.2-7 13-7 13S5 14.2 5 9a7 7 0 0 1 7-7zm0 4.5A2.5 2.5 0 1 0 12 11.5 2.5 2.5 0 0 0 12 6.5z"/></svg></span>
          <span>42 Orchard Lane<br>Fairview, NY 14099</span>
        </li>
      </ul>
    </div>
  </section>

</main>
</body>
</html>
```